Rally 84 Training is our company name. and instruction

We provide emergency medical training for CPR (Cardiopulmonary Resuscitation) /AED (Automated External Defibrillation) , BLS (Basic Life Support, First Aid, Bloodborne Pathogens
We travel to the client, give certified (CVL) Continental Vitality League (CVL) instruction for job/industry certification in the areas listed.
CVL Kin and Neighbors noncertified instruction

Target Market(s)

Medical professionals, job required certification

Industry/Entity Type

Medical And Science

Contact Information for Business Card

Logo
Phone, email, address, website address, FB, Instagram

Font styles to use
Serif
Sans Serif

Colors
fff2fe
ff1b2f

Requirements
Must have
• Logo
Course taught: CPR (Cardiopulmonary Resuscitation)
AED (Automated External Defibrillation)
First Aid
BLS (Basic Life Support)
Bloodborne Pathogens
Offsite instruction - we come to you
Nice to have
• Red/Black scheme
Possible ecg/heart rhythm design
Should not have
• Cartoon images

```html
<!DOCTYPE html>
<html lang="en">
<head>
<meta charset="UTF-8">
<title>Rally 84 Training — Business Card</title>
<link rel="stylesheet" href="https://fonts.googleapis.com/css2?family=Poppins:wght@400;500;600&display=swap">
<style>
  :root {
    --stage: #2a2a2c;
    --card-light: #ffffff;
    --card-light-shade: #eceaf0;
    --card-dark: #0d0d0d;
    --brand-red: #ff1b2f;
    --ink: #222222;
    --ring: #1a1a1a;
  }
  * { box-sizing: border-box; margin: 0; padding: 0; }
  html, body { width: 1200px; height: 900px; overflow: hidden; }
  body {
    background: var(--stage);
    font-family: "Poppins", sans-serif;
    display: flex;
    flex-direction: column;
    align-items: center;
    justify-content: center;
    gap: 40px;
  }
  .card {
    position: relative;
    width: 630px;
    height: 360px;
    border-radius: 4px;
    overflow: hidden;
    box-shadow: 0 10px 30px rgba(0,0,0,0.45);
  }
  .card--front {
    background: linear-gradient(135deg, var(--card-light-shade) 0%, var(--card-light) 55%);
    color: var(--ink);
  }
  .card--back { background: var(--card-dark); }

  .address {
    position: absolute;
    left: 48px; top: 44px;
    font-size: 15px;
    line-height: 1.45;
  }
  .contact-list {
    position: absolute;
    left: 48px; top: 176px;
    list-style: none;
    font-size: 15px;
    line-height: 1.2;
  }
  .contact-list li { display: flex; align-items: center; gap: 10px; margin-bottom: 7px; }
  .contact-icon { width: 20px; height: 20px; flex: none; }

  .ecg-line {
    position: absolute;
    left: 300px; top: 120px;
    width: 330px; height: 120px;
  }

  .brand {
    position: absolute;
    display: flex;
    flex-direction: column;
    align-items: center;
    gap: 10px;
  }
  .card--front .brand { right: 40px; top: 96px; }
  .card--back .brand { right: 44px; top: 96px; }
  .brand-disc {
    width: 130px; height: 130px;
    border-radius: 50%;
    background: var(--brand-red);
    border: 5px solid var(--ring);
    box-shadow: 0 0 0 3px #ffffff;
  }
  .card--front .brand-disc { box-shadow: none; }
  .brand-name {
    font-size: 16px;
    font-weight: 600;
    color: var(--brand-red);
    white-space: nowrap;
  }

  .course-list {
    position: absolute;
    left: 36px; top: 64px;
    list-style: none;
    color: var(--brand-red);
    font-size: 14.5px;
    line-height: 1.3;
    max-width: 380px;
  }
  .course-list li { display: flex; align-items: flex-start; gap: 8px; margin-bottom: 9px; }
  .pulse-mark { width: 24px; height: 14px; flex: none; margin-top: 2px; }
</style>
</head>
<body>

<section class="card card--front" aria-label="Business card front">
  <p class="address">418 Larkspur Avenue NE<br>Suite 210, Fenwick Falls<br>MI 49871</p>

  <ul class="contact-list">
    <li>
      <svg class="contact-icon" viewBox="0 0 20 20" aria-hidden="true"><circle cx="10" cy="10" r="10" fill="#ff1b2f"/><path d="M7 5.5l2 2-1 1.3a6 6 0 0 0 3.2 3.2l1.3-1 2 2-1.2 1.5c-3.6-.3-7-3.7-7.3-7.3z" fill="#fff"/></svg>
      61 470 228 934
    </li>
    <li>
      <svg class="contact-icon" viewBox="0 0 20 20" aria-hidden="true"><circle cx="10" cy="10" r="10" fill="#ff1b2f"/><rect x="5" y="6.5" width="10" height="7" fill="none" stroke="#fff" stroke-width="1.2"/><path d="M5 6.5l5 4 5-4" fill="none" stroke="#fff" stroke-width="1.2"/></svg>
      info@rally84training.com
    </li>
    <li>
      <svg class="contact-icon" viewBox="0 0 20 20" aria-hidden="true"><circle cx="10" cy="10" r="10" fill="#ff1b2f"/><circle cx="10" cy="10" r="5" fill="none" stroke="#fff" stroke-width="1.1"/><path d="M5 10h10M10 5c-2 3-2 7 0 10M10 5c2 3 2 7 0 10" fill="none" stroke="#fff" stroke-width="1.1"/></svg>
      www.rally84training.com
    </li>
    <li>
      <svg class="contact-icon" viewBox="0 0 20 20" aria-hidden="true"><circle cx="10" cy="10" r="10" fill="#ff1b2f"/></svg>
      @rally84training
    </li>
    <li>
      <svg class="contact-icon" viewBox="0 0 20 20" aria-hidden="true"><circle cx="10" cy="10" r="10" fill="#ff1b2f"/></svg>
      rally84training
    </li>
  </ul>

  <svg class="ecg-line" viewBox="0 0 330 120" aria-hidden="true">
    <circle cx="4" cy="58" r="3" fill="#ff1b2f"/>
    <polyline points="4,58 30,58 36,48 42,70 48,40 54,62 60,58 80,58 86,52 92,66 98,44 104,60 110,58 150,58" fill="none" stroke="#ff1b2f" stroke-width="1.6"/>
  </svg>

  <div class="brand">
    <div class="brand-disc"></div>
    <span class="brand-name">Rally 84 Training</span>
  </div>
</section>

<section class="card card--back" aria-label="Business card back">
  <ul class="course-list">
    <li><svg class="pulse-mark" viewBox="0 0 24 14" aria-hidden="true"><polyline points="0,8 7,8 9,3 12,13 15,1 17,8 24,8" fill="none" stroke="#ff1b2f" stroke-width="1.5"/></svg>CPR (Cardiopulmonary Resuscitation)</li>
    <li><svg class="pulse-mark" viewBox="0 0 24 14" aria-hidden="true"><polyline points="0,8 7,8 9,3 12,13 15,1 17,8 24,8" fill="none" stroke="#ff1b2f" stroke-width="1.5"/></svg>AED (Automated External Defibrillation)</li>
    <li><svg class="pulse-mark" viewBox="0 0 24 14" aria-hidden="true"><polyline points="0,8 7,8 9,3 12,13 15,1 17,8 24,8" fill="none" stroke="#ff1b2f" stroke-width="1.5"/></svg>First Aid</li>
    <li><svg class="pulse-mark" viewBox="0 0 24 14" aria-hidden="true"><polyline points="0,8 7,8 9,3 12,13 15,1 17,8 24,8" fill="none" stroke="#ff1b2f" stroke-width="1.5"/></svg>BLS (Basic Life Support)</li>
    <li><svg class="pulse-mark" viewBox="0 0 24 14" aria-hidden="true"><polyline points="0,8 7,8 9,3 12,13 15,1 17,8 24,8" fill="none" stroke="#ff1b2f" stroke-width="1.5"/></svg>Bloodborne Pathogens</li>
    <li><svg class="pulse-mark" viewBox="0 0 24 14" aria-hidden="true"><polyline points="0,8 7,8 9,3 12,13 15,1 17,8 24,8" fill="none" stroke="#ff1b2f" stroke-width="1.5"/></svg>Offsite instruction - we come to you</li>
  </ul>

  <div class="brand">
    <div class="brand-disc"></div>
    <span class="brand-name">Rally 84 Training</span>
  </div>
</section>

</body>
</html>
```